Tall Glass Web site design

The aim of Tall Glass is to provide an online service which allows customers to pre-order drinks and gain incentives such as fast entry, special offers (drinks, entry fees), as well as allowing customers to compare drinking establishments based upon costs and ratings.

what is required is the design of the pages stated below completed to the specifications.

Target Market(s)

The target market of Tall Glass is men and women between the ages of 18 to 26 mainly. Within the age range of 18 to 26 the more specific target groups

Industry/Entity Type

Online

Requirements
Must have
• What is required to be designed

Website to be viewable on different systems e.g desktop, laptop and for mobile devices a mobile friendly page

Home page

Logo
Company name
Log in
Sign up
Help
Social media links, Follow us link

Bar, pub, club search function
Search by postcode, establishment type, distance

Pictorial instructions of how to use the site like ( plate hop). The stages are 1) select location 2) build order and pay 3) pick up from bar

Pre load results of establishments

Drinking establishment sign up

Map showing search results

List of results

My basket window which shows your order

Pop out box for customer sign up

Buttons for FAQ, general information, company information, Privacy policy ect at bottom of page

The home page is required to be Clear, simple, easy to use and stylish but not over the top with to much information which will confuse the customers. The preloaded results need to be obvious and where can be seen. The pictorial instructions should go below the preloaded results. Once the search criteria has been filled in and has been submitted the preloaded results and pictorial instructions will be removed and be replaced by the map and search results.

Drinking establishment personal page requires

Details of drinking establishment (name, address, contact, map)
list of drinks avliable
My basket
Special Offers
Gallery
Calendar
Reviews section at the bottom

When a person clicks on a drinking establishment page what that person should see when they open the page is company name logo
with a list of the drinks they offer and special offers. Tabs or buttons for gallery, establishment details, calender and special offers should be located along top or down the left. when they are clicked on they will replace the menu.

The colour scheme is based around the logo which is attached. We do not want any pink or overly bright colours which would not go with the logo.

A site which we like is this one
http://www.plate-hop.example/
this site is perfect simple, clear but also good looking. If you need inspiration you should use this site as a starting point.
Should not have
• what should be avoided is a site which like this one http://forkwagon.example/~beta/?gclid=XQPLmWeRtyuKAbNHsZcDvFGHIj

it is to complicated with bad font and colours. The site just feels cheesy and not classy. we like very little about this site

```html
<!DOCTYPE html>
<html lang="en">
<head>
<meta charset="utf-8">
<title>Tall Glass – Drinking Establishment</title>
<link rel="stylesheet" href="https://fonts.googleapis.com/css2?family=Open+Sans:wght@400;600;700&family=Gochi+Hand&display=swap">
<style>
:root{
  --navy:#2e3192;
  --navy-dark:#262a7c;
  --blue-btn-top:#6d70e0;
  --blue-btn-bot:#3b3fc0;
  --text:#333;
  --muted:#555;
  --grey-line:#d6d6d6;
  --dash:#b8b8b8;
  --panel:#bdbdbd;
  --gold:#d9a21b;
  --page:#fff;
}
*{box-sizing:border-box;margin:0;padding:0}
html,body{width:1187px;height:1200px;overflow:hidden;background:var(--page)}
body{position:relative;font-family:"Open Sans",Arial,sans-serif;color:var(--text)}
.abs{position:absolute}
.top-edge{left:0;top:0;width:1187px;height:6px;background:#bfbfbf}

/* header */
.brand{left:184px;top:18px;display:flex;align-items:center;gap:10px}
.brand-mark{width:72px;height:72px;border-radius:50%;background:#8a8a8a}
.brand-name{font-size:31px;font-weight:600;color:var(--navy)}
.social{display:flex;gap:4px}
.social span{width:22px;height:22px;border-radius:50%;background:var(--navy);display:block}
.social.head{left:903px;top:25px}
.cart{left:551px;top:60px;display:flex;align-items:center;font-size:12.7px;color:var(--muted)}
.cart svg{margin-right:5px}
.cart b{color:#2b4fd8;font-weight:700;margin-right:3px}
.cart .sum{color:#2b4fd8;font-weight:700;margin-left:3px}
.btn-checkout{margin-left:8px;width:72px;height:20px;border:1px solid #aaa;background:linear-gradient(#eee,#cfcfcf);font-size:12.5px;color:#444;display:flex;align-items:center;justify-content:center}
.account{left:816px;top:60px;font-size:14px;font-weight:700;color:#555}
.help{left:927px;top:59px;width:80px;height:23px;border:1px solid #bbb;border-radius:4px;font-size:12px;color:var(--navy);display:flex;align-items:center;justify-content:center;background:#fff;box-shadow:0 1px 2px rgba(0,0,0,.2)}
.rule{left:181px;top:123px;width:821px;height:1px;background:var(--grey-line)}
.page-title{left:183px;top:128px;font-family:"Gochi Hand",cursive;font-size:28px;color:var(--navy)}

/* sidebar */
.map{left:181px;top:184px;width:197px;height:161px;border:1px solid #ccc;padding:5px;background:#fff}
.map div{width:100%;height:100%;background:linear-gradient(135deg,#e9e4d8,#cfe3b8 60%,#d8d2c2)}
.side-nav{left:181px;top:355px;width:196px;list-style:none}
.side-nav li{height:31px;margin-bottom:8px;border:1px solid #b5b5b5;background:linear-gradient(#ececec,#cdcdcd);display:flex;align-items:center;padding-left:10px;font-size:13.5px;color:#444}
.side-nav svg{margin-right:9px}
.creator{left:181px;top:558px;width:194px;height:241px;background:var(--panel);padding:14px 17px}
.creator h3{font-family:"Gochi Hand",cursive;font-weight:400;font-size:24px;color:var(--navy);line-height:26px}
.creator p{font-size:13.5px;color:#333;margin:2px 0 6px}
.select{height:30px;background:#fff;border:1px solid #ccc;display:flex;align-items:center;justify-content:space-between;padding:0 8px;font-size:13.5px;color:#555;margin-bottom:8px}
.select i{border:4px solid transparent;border-top:5px solid #333;margin-top:4px}
.btn-search{margin-top:12px;width:156px;height:32px;border-radius:3px;background:linear-gradient(var(--blue-btn-top),var(--blue-btn-bot));color:#fff;font-weight:700;font-size:16px;display:flex;align-items:center;justify-content:center;gap:6px;box-shadow:0 1px 2px rgba(0,0,0,.3)}

/* venue */
.venue-photo{left:396px;top:184px;width:108px;height:108px;background:linear-gradient(#5a5048,#2a2726);box-shadow:0 1px 3px rgba(0,0,0,.4)}
.venue{left:521px;top:179px}
.venue h1{font-size:18px;font-weight:700;color:var(--navy);margin-bottom:2px}
.venue dl{display:grid;grid-template-columns:92px auto;row-gap:3px;font-size:12.5px;line-height:17px}
.venue dt{font-weight:700;color:#444}
.venue dd{color:#555}
.cost{color:var(--gold);font-weight:700;letter-spacing:3px}
.rating{display:inline-flex;gap:4px;vertical-align:middle}
.when{left:855px;top:205px;font-size:12.5px;font-weight:700;color:#444}
.when .select{margin-top:8px;width:136px;height:32px;border-radius:2px;box-shadow:0 1px 2px rgba(0,0,0,.15)}
.divider{left:396px;top:312px;width:599px;border-top:1px dashed var(--dash)}

/* offers */
.offers{left:396px;top:326px;width:599px}
.offers h2{font-family:"Gochi Hand",cursive;font-weight:400;font-size:23px;color:#444;height:30px;margin-bottom:8px}
.category h3{font-size:15.5px;font-weight:700;color:var(--navy);line-height:20px;margin-bottom:10px}
.category + .category h3{margin-top:26px}
.row{display:grid;grid-template-columns:293px 293px;gap:13px}
.row + .row{margin-top:17px}
.card{display:flex;padding-bottom:17px;border-bottom:1px dashed var(--dash)}
.thumb{width:71px;height:72px;flex:none;border:1px solid #bbb}
.info{margin-left:6px}
.info h4{font-size:14.5px;font-weight:700;color:#333;line-height:18px;margin-top:-3px}
.info p{font-size:12.5px;color:#444;margin-top:3px;white-space:nowrap}
.actions{display:flex;gap:6px;margin-top:7px}
.qty{width:75px;height:30px;border:1px solid #ccc;font-size:12.5px;color:#555;display:flex;align-items:center;justify-content:center;margin-top:1px}
.btn-add{width:117px;height:32px;border-radius:3px;background:linear-gradient(var(--blue-btn-top),var(--blue-btn-bot));color:#fff;font-weight:700;font-size:14.5px;display:flex;align-items:center;justify-content:center;box-shadow:0 1px 2px rgba(0,0,0,.3)}

/* footer */
.footer{left:0;top:1095px;width:1187px;height:105px;background:var(--navy)}
.footer-links{left:179px;top:1122px;font-size:13px;color:#fff}
.footer-links span{margin:0 4px}
.copy{left:179px;top:1148px;font-size:13px;color:#b9bbe6}
.social.foot{left:895px;top:1135px;gap:4px}
.social.foot span{background:#fff;width:22px;height:22px}
</style>
</head>
<body>
<div class="abs top-edge"></div>

<header>
  <div class="abs brand"><span class="brand-mark"></span><span class="brand-name">Tall Glass</span></div>
  <div class="abs social head"><span></span><span></span><span></span><span></span></div>
  <div class="abs cart">
    <svg width="14" height="12" viewBox="0 0 14 12"><path d="M0 1h3l2 7h7l2-5H4" fill="none" stroke="#555" stroke-width="1.6"/><circle cx="6" cy="10.5" r="1.3" fill="#555"/><circle cx="11" cy="10.5" r="1.3" fill="#555"/></svg>
    <b>0</b>items | Subtotal :<span class="sum">£0.0</span>
    <span class="btn-checkout">Checkout</span>
  </div>
  <div class="abs account">Log in . Sign up</div>
  <div class="abs help">NEED HELP</div>
</header>
<div class="abs rule"></div>
<div class="abs page-title">Drinking Establishment</div>

<aside>
  <div class="abs map"><div role="img" aria-label="Street map showing the establishment's location"></div></div>
  <ul class="abs side-nav">
    <li><svg width="16" height="14"><path d="M2 7l6-6h7v7l-6 6z" fill="#888"/></svg>ENTRY TICKETS</li>
    <li><svg width="16" height="16"><circle cx="8" cy="8" r="6" fill="#888"/></svg>SPECIAL OFFERS</li>
    <li><svg width="16" height="15"><rect x="1" y="2" width="14" height="12" fill="none" stroke="#888" stroke-width="2"/><path d="M1 6h14" stroke="#888" stroke-width="2"/></svg>CALENDER</li>
    <li><svg width="16" height="14"><rect x="1" y="1" width="14" height="12" fill="none" stroke="#888" stroke-width="2"/><path d="M3 11l4-5 3 3 2-2 2 4z" fill="#888"/></svg>GALLERY</li>
    <li><svg width="16" height="12"><rect x="1" y="1" width="14" height="10" fill="#888"/><path d="M1 1l7 6 7-6" fill="none" stroke="#ddd" stroke-width="1.4"/></svg>CONTACT DETAILS</li>
  </ul>
  <form class="abs creator">
    <h3>Drink creator</h3>
    <p>Drink Type</p>
    <div class="select">Ingredient 1<i></i></div>
    <div class="select">Ingredient 2<i></i></div>
    <div class="select">Ingredient 3<i></i></div>
    <div class="btn-search">SEARCH NOW <svg width="18" height="18"><circle cx="7" cy="7" r="5" fill="none" stroke="#fff" stroke-width="2.2"/><path d="M11 11l5 5" stroke="#fff" stroke-width="2.5"/></svg></div>
  </form>
</aside>

<main>
  <div class="abs venue-photo" role="img" aria-label="Photo of the pub frontage"></div>
  <section class="abs venue">
    <h1>The LANTERN</h1>
    <dl>
      <dt>Provides</dt><dd>: Food &amp; Drink</dd>
      <dt>Special offers</dt><dd>: 15% Off</dd>
      <dt>Cost</dt><dd>: <span class="cost">£££££</span></dd>
      <dt>Rating</dt><dd>: <span class="rating">
        <svg width="16" height="13"><rect x="1" y="1" width="10" height="11" fill="#3b3fc0"/><path d="M11 4h3v5h-3" fill="none" stroke="#3b3fc0" stroke-width="1.6"/></svg>
        <svg width="16" height="13"><rect x="1" y="1" width="10" height="11" fill="#3b3fc0"/><path d="M11 4h3v5h-3" fill="none" stroke="#3b3fc0" stroke-width="1.6"/></svg>
        <svg width="16" height="13"><rect x="1" y="1" width="10" height="11" fill="#3b3fc0"/><path d="M11 4h3v5h-3" fill="none" stroke="#3b3fc0" stroke-width="1.6"/></svg>
        <svg width="16" height="13"><rect x="1" y="1" width="10" height="11" fill="#3b3fc0"/><path d="M11 4h3v5h-3" fill="none" stroke="#3b3fc0" stroke-width="1.6"/></svg>
        <svg width="16" height="13"><rect x="1" y="1" width="10" height="11" fill="#bbb"/><path d="M11 4h3v5h-3" fill="none" stroke="#bbb" stroke-width="1.6"/></svg>
      </span></dd>
    </dl>
  </section>
  <div class="abs when">When do you want to go<div class="select">Select Order Day<i></i></div></div>
  <div class="abs divider"></div>

  <section class="abs offers">
    <h2>Establishment also offers</h2>

    <div class="category">
      <h3>Wines</h3>
      <div class="row">
        <article class="card"><div class="thumb" role="img" aria-label="Red wine being poured" style="background:linear-gradient(135deg,#f4e8e8,#8d1a2a)"></div><div class="info"><h4>Duis sed lectus sit amet</h4><p>Nulla cursus ligula nec neque porttitor</p><div class="actions"><span class="qty">How Many</span><span class="btn-add">ADD TO ORDER</span></div></div></article>
        <article class="card"><div class="thumb" role="img" aria-label="Glass of red wine outdoors" style="background:linear-gradient(#7d9a4a,#9a1b2b 60%,#4a5a2a)"></div><div class="info"><h4>Donec non urna et ligula</h4><p>Etiam tempor sapien ac arcu</p><div class="actions"><span class="qty">How Many</span><span class="btn-add">ADD TO ORDER</span></div></div></article>
      </div>
      <div class="row">
        <article class="card"><div class="thumb" role="img" aria-label="Wine glass with red wine" style="background:radial-gradient(circle at 50% 55%,#6a1010,#c89a5a 70%,#e8c890)"></div><div class="info"><h4>Nullam nisi risus</h4><p>Nullam enim magna, laoreet ut</p><div class="actions"><span class="qty">How Many</span><span class="btn-add">ADD TO ORDER</span></div></div></article>
        <article class="card"><div class="thumb" role="img" aria-label="Wine poured from a bottle" style="background:linear-gradient(135deg,#f2f2f2,#d8d8d8 50%,#b01a2a)"></div><div class="info"><h4>Maecenas non lorem</h4><p>Praesent et nulla nisl</p><div class="actions"><span class="qty">How Many</span><span class="btn-add">ADD TO ORDER</span></div></div></article>
      </div>
    </div>

    <div class="category">
      <h3>Beers</h3>
      <div class="row">
        <article class="card"><div class="thumb" role="img" aria-label="Splashing glass of beer" style="background:radial-gradient(circle,#e8c060,#5a3a10)"></div><div class="info"><h4>Duis sed lectus sit amet</h4><p>Nulla cursus ligula nec neque porttitor</p><div class="actions"><span class="qty">How Many</span><span class="btn-add">ADD TO ORDER</span></div></div></article>
        <article class="card"><div class="thumb" role="img" aria-label="Row of beer glasses" style="background:linear-gradient(#f0e8d8,#d08a2a 55%,#8a5a2a)"></div><div class="info"><h4>Donec non urna et ligula</h4><p>Etiam tempor sapien ac arcu</p><div class="actions"><span class="qty">How Many</span><span class="btn-add">ADD TO ORDER</span></div></div></article>
      </div>
    </div>

    <div class="category">
      <h3>Cocktails</h3>
      <div class="row">
        <article class="card"><div class="thumb" role="img" aria-label="Red cocktails at a bar" style="background:linear-gradient(#c02010,#e8401a 60%,#8a1008)"></div><div class="info"><h4>Duis sed lectus sit amet</h4><p>Nulla cursus ligula nec neque porttitor</p><div class="actions"><span class="qty">How Many</span><span class="btn-add">ADD TO ORDER</span></div></div></article>
        <article class="card"><div class="thumb" role="img" aria-label="Cocktail glasses on a table" style="background:linear-gradient(#a8b8a0,#e05a4a 55%,#6a7a5a)"></div><div class="info"><h4>Donec non urna et ligula</h4><p>Etiam tempor sapien ac arcu</p><div class="actions"><span class="qty">How Many</span><span class="btn-add">ADD TO ORDER</span></div></div></article>
      </div>
    </div>

    <div class="category">
      <h3>Non alcoholic</h3>
      <div class="row">
        <article class="card"><div class="thumb" role="img" aria-label="Orange fruit drink with straw" style="background:radial-gradient(circle at 50% 45%,#f0501a,#fbd0b0 55%,#fff)"></div><div class="info"><h4>Duis sed lectus sit amet</h4><p>Nulla cursus ligula nec neque porttitor</p><div class="actions"><span class="qty">How Many</span><span class="btn-add">ADD TO ORDER</span></div></div></article>
        <article class="card"><div class="thumb" role="img" aria-label="Strawberry smoothie" style="background:linear-gradient(135deg,#cde8b0,#f4c8c0 55%,#c0202a)"></div><div class="info"><h4>Donec non urna et ligula</h4><p>Etiam tempor sapien ac arcu</p><div class="actions"><span class="qty">How Many</span><span class="btn-add">ADD TO ORDER</span></div></div></article>
      </div>
    </div>
  </section>
</main>

<footer>
  <svg class="abs" style="left:0;top:1089px" width="1187" height="8" viewBox="0 0 1187 8" preserveAspectRatio="none"><path d="M0 6L30 4 60 6 95 3 130 5 170 2 210 5 250 3 300 6 340 3 390 5 440 2 490 5 540 3 590 6 640 3 690 5 740 2 790 5 840 3 890 6 940 3 990 5 1040 2 1090 5 1140 3 1187 5V8H0z" fill="#2e3192"/></svg>
  <div class="abs footer"></div>
  <nav class="abs footer-links">FAQ<span>|</span>general information<span>|</span>company information<span>|</span>Privacy policy</nav>
  <p class="abs copy">Copyright © 2013 Tall Glass. All rights reserved</p>
  <div class="abs social foot"><span></span><span></span><span></span><span></span></div>
</footer>
</body>
</html>
```